QUOTE Graphics for Summer Challenge

I would like to put these quotes over one of the pictures attached; For Instagram, use new size: 4:5 (1080 x 1350 pixels). One Quote per picture, and I want the quote to be bold or easy to read as well. I provided a few reference graphics that I really like as examples below.
All of the pictures are attached; you can pick any photo and add one quote to it; but no stock photography
All the quotes are in the attached WORD document

```html
<!DOCTYPE html>
<html lang="en">
<head>
<meta charset="utf-8">
<title>Sun Girl Summer Shapeup – Quote Graphics</title>
<link rel="stylesheet" href="https://fonts.googleapis.com/css2?family=Roboto+Condensed:wght@400;700&display=swap">
<style>
  :root{
    --white:#ffffff;
    --ink:#111111;
    --page:#ffffff;
    --coral:#f07577;
    --rose:#d4666c;
    --plum:#7b3564;
    --berry:#a5416e;
    --pink:#e85a82;
    --hotpink:#f25c84;
    --teal:#0a86a6;
    --deepteal:#05485e;
    --nightteal:#0d4656;
    --violet:#6f3a6e;
  }
  *{box-sizing:border-box;margin:0;padding:0}
  html,body{width:740px;height:1200px;overflow:hidden;background:var(--page)}
  body{position:relative;font-family:"Roboto Condensed",sans-serif;font-weight:700;color:var(--white);text-transform:uppercase}
  .card{position:absolute;width:214px;height:267px;overflow:hidden}
  .row{position:absolute;left:0;right:0;text-align:center}
  .quote{font-size:15px;line-height:16.5px}
  .rule{position:absolute;height:2px;background:var(--white)}
  .tag{display:inline-block;background:var(--white);color:var(--ink);padding:0 4px;line-height:1.15}
  .band{position:absolute;left:0;right:0}
  .cta{font-size:10.5px;line-height:11.5px}
  .handle{font-size:5px;font-weight:400;letter-spacing:.1px}

  .card--jumpstart{left:42px;top:21px;background:linear-gradient(150deg,var(--rose),var(--plum))}
  .card--waist{left:264px;top:21px;background:linear-gradient(150deg,#7a3765,var(--coral))}
  .card--scale{left:483px;top:21px;background:linear-gradient(180deg,var(--berry),var(--pink) 70%,#d9507a)}
  .card--detox{left:42px;top:295px;background:linear-gradient(180deg,var(--teal),#4a4f7c 55%,var(--violet))}
  .card--plan{left:264px;top:295px;background:linear-gradient(180deg,#0b7d9c,var(--deepteal))}
  .card--ready{left:483px;top:295px;background:linear-gradient(180deg,#0a88a8,#5a4679 55%,#7d3566)}
  .card--helping{left:42px;top:569px;background:linear-gradient(160deg,var(--nightteal),#8b6170 55%,var(--coral))}
  .card--cravings{left:264px;top:569px;background:linear-gradient(180deg,#0682a3,#06485d)}
  .card--bloat{left:483px;top:569px;background:linear-gradient(180deg,#0f4657,#9c4d73 55%,var(--hotpink))}
  .card--sluggish{left:265px;top:843px;background:linear-gradient(30deg,#1f8bab,#8b7a93 50%,var(--coral))}
</style>
</head>
<body>

<section class="card card--jumpstart">
  <p class="row quote" style="top:40px;font-size:16px">“IF YOU FEEL LIKE<br>YOU’VE LET YOURSELF<br>GO LATELY”</p>
  <div class="rule" style="top:101px;left:72px;width:69px;height:1.5px"></div>
  <p class="row" style="top:107px;font-size:13px;line-height:13px">THIS IS YOUR<br>JUMPSTART</p>
  <div class="rule" style="top:138px;left:72px;width:69px;height:1.5px"></div>
  <div class="band" style="top:166px;left:41px;width:132px;height:49px;background:rgba(110,40,80,.55)"></div>
  <p class="row cta" style="top:169px"><span class="tag">COMMENT SUMMER</span><br>TO JOIN THE SUN GIRL<br>SUMMER SHAPEUP</p>
  <p class="row handle" style="top:247px">@GLOWSTUDIOONLINE</p>
</section>

<section class="card card--waist">
  <p class="row quote" style="top:39px">“ WE’RE GETTING<br>A TINY WAIST<br>AND DROPPING POUNDS<br>TOGETHER.”</p>
  <div class="rule" style="top:121px;left:50px;width:113px;height:3px"></div>
  <p class="row" style="top:127px"><span class="tag" style="width:113px;font-size:13px;line-height:19px">DON’T MISS THIS</span></p>
  <div class="rule" style="top:150px;left:50px;width:113px;height:3px"></div>
  <div class="band" style="top:174px;left:27px;width:160px;height:37px;background:rgba(130,50,80,.6)"></div>
  <p class="row" style="top:178px;font-size:12.5px;line-height:14px"><span class="tag">COMMENT SUN GIRL</span><br>TO JOIN</p>
  <p class="row handle" style="top:234px">@GLOWSTUDIOONLINE</p>
</section>

<section class="card card--scale">
  <p class="row quote" style="top:38px;line-height:17px">“THE SCALE KEEPS<br>CLIMBING AND<br>NOTHING’S<br>WORKING?</p>
  <div class="rule" style="top:116px;left:41px;width:132px;height:1px"></div>
  <p class="row" style="top:121px;font-size:17px;line-height:20px">THIS CHALLENGE IS<br>YOUR LIFELINE.”</p>
  <div class="rule" style="top:165px;left:41px;width:132px;height:1px"></div>
  <div class="band" style="top:181px;height:38px;background:rgba(255,255,255,.16)"></div>
  <p class="row" style="top:184px;font-size:14px;line-height:16px"><span class="tag" style="width:132px">COMMENT SUN GIRL</span><br>TO JOIN NOW!</p>
  <p class="row handle" style="top:244px">@GLOWSTUDIOONLINE</p>
</section>

<section class="card card--detox">
  <p class="row" style="top:39px"><span class="tag" style="font-size:13px;line-height:22px;width:130px">NEED A JUMPSTART?</span></p>
  <p class="row quote" style="top:85px;font-size:16px;line-height:15.5px">“DETOXING,<br>BURNING FAT, AND<br>GETTING SNATCHED.”</p>
  <div class="rule" style="top:136px;left:36px;width:141px"></div>
  <div class="band" style="top:170px;height:51px;background:rgba(60,45,90,.55)"></div>
  <p class="row" style="top:173px;font-size:11.5px;line-height:13.5px"><span class="tag">COMMENT SUN GIRL</span><br>TO JOIN US ON<br><span style="font-size:13.5px">JULY 7TH</span></p>
  <p class="row handle" style="top:244px">@GLOWSTUDIOONLINE</p>
</section>

<section class="card card--plan">
  <p class="row" style="top:32px"><span class="tag" style="width:105px;text-align:left;font-size:13px;line-height:15px;padding:2px 5px">YOU DON’T NEED<br>MOTIVATION</span></p>
  <p class="row quote" style="top:76px;font-size:16px;line-height:18px">“YOU NEED<br>A PROVEN PLAN<br>AND SOME<br>ACCOUNTABILITY.”</p>
  <div class="rule" style="top:151px;left:56px;width:103px"></div>
  <div class="band" style="top:174px;left:45px;width:125px;height:45px;background:rgba(4,60,78,.7)"></div>
  <p class="row cta" style="top:178px;font-size:10px"><span class="tag">COMMENT SUN GIRL</span><br>TO GET JOIN US<br>JULY 7TH</p>
  <p class="row handle" style="top:238px">@GLOWSTUDIOONLINE</p>
</section>

<section class="card card--ready">
  <p class="row" style="top:37px"><span class="tag" style="width:117px;font-size:15px;line-height:25px">SUMMER’S HERE</span></p>
  <p class="row quote" style="top:75px;left:52px;right:58px;text-align:right;font-size:14px;line-height:14px">“BUT YOUR BODY<br>DOESN’T<br>FEEL READY?<br>YOU’RE<br>NOT TOO LATE.”</p>
  <div class="rule" style="top:154px;left:53px;width:108px"></div>
  <div class="band" style="top:171px;left:34px;width:147px;height:52px;background:rgba(60,35,70,.6)"></div>
  <p class="row cta" style="top:175px;font-size:11.5px;line-height:13px"><span class="tag">COMMENT SUMMER</span><br>TO JOIN THE SUN GIRL<br>SUMMER SHAPEUP</p>
  <p class="row handle" style="top:244px">@GLOWSTUDIOONLINE</p>
</section>

<section class="card card--helping">
  <p class="row quote" style="top:40px;line-height:16.8px">“THIS SUN GIRL<br>SUMMER SHAPEUP<br>PLAN IS HELPING<br>WOMEN<br>DROP POUNDS AND<br>FEEL SEXY AGAIN.”</p>
  <div class="rule" style="top:148px;left:41px;width:132px"></div>
  <div class="band" style="top:173px;height:40px;background:rgba(80,60,70,.55)"></div>
  <p class="row" style="top:177px;font-size:14px;line-height:16px"><span class="tag">COMMENT SUMMER</span><br>TO JOIN US</p>
  <p class="row handle" style="top:240px">@GLOWSTUDIOONLINE</p>
</section>

<section class="card card--cravings">
  <p class="row quote" style="top:52px;line-height:16.3px">“CRAVINGS, BELLY FAT,<br>AND WATER WEIGHT?<br><span class="tag" style="width:131px;color:#0b5f78;font-size:15px">SAY GOODBYE IN</span><br>30 DAYS.”</p>
  <div class="band" style="top:158px;left:31px;width:152px;height:56px;background:rgba(4,70,90,.7)"></div>
  <p class="row cta" style="top:161px;font-size:10.5px;line-height:12px"><span class="tag">COMMENT SUMMER</span><br>TO JOIN<br>THE SUN GIRL<br>SUMMER SHAPEUP</p>
  <p class="row handle" style="top:241px">@GLOWSTUDIOONLINE</p>
</section>

<section class="card card--bloat">
  <p class="row quote" style="top:37px;line-height:15px">“YOUR BELLY BLOAT<br>AND STUBBORN<br>WEIGHT GAIN<br>AREN’T GOING<br>ANYWHERE..”</p>
  <p class="row" style="top:120px"><span class="tag" style="width:76px;font-size:10px;line-height:12.5px;padding:3px 2px">UNLESS YOU<br>DO SOMETHING<br>DIFFERENT.</span></p>
  <div class="rule" style="top:171px;left:69px;width:76px"></div>
  <div class="band" style="top:190px;height:30px;background:rgba(255,255,255,.14)"></div>
  <p class="row" style="top:192px;font-size:11.5px;line-height:12.5px"><span class="tag">COMMENT SUN GIRL</span><br>TO JOIN US.!</p>
  <p class="row handle" style="top:248px">@GLOWSTUDIOONLINE</p>
</section>

<section class="card card--sluggish">
  <p class="row quote" style="top:45px;font-size:17px;line-height:17.5px">“FEELING BLOATED,<br>SLUGGISH,<br>AND TOO BIG?<br>YOUR DETOX<br>STARTS NOW.”</p>
  <p class="row" style="top:152px;font-size:12.5px;line-height:14.3px"><span class="tag">COMMENT SUMMER</span><br>TO JOIN<br>THE SUN GIRL<br>SUMMER SHAPEUP</p>
  <div class="rule" style="top:213px;left:60px;width:94px;height:1.5px"></div>
  <p class="row handle" style="top:246px">@GLOWSTUDIOONLINE</p>
</section>

</body>
</html>
```